Stationary for an International Church

We need a design for various stationery items - letters/envelopes, Word/PowerPoint pages, based on
- the MBF Logo
- the primary color "bright turquoise" ("vivid cyan"), hex #08e8de
- the font family: Frutiger 55 Roman
To get an image of our organization, please visit velmarhall.org, recent blog entries at https://www.velmarhall.org/blog or annual reports at Downloads

Target Market(s)

Congregation and business partners of the Chruch

Font styles to use
Other font styles liked:
• requirement: Frutiger 55 Roman

Colors
33b8a4

Requirements
Must have
• simple, modern design, a bit unique

```html
<!DOCTYPE html>
<html lang="en">
<head>
<meta charset="utf-8">
<title>Mercer Bay Fellowship – Stationery</title>
<link rel="stylesheet" href="https://fonts.googleapis.com/css2?family=Hind:wght@400;500;600&display=swap">
<style>
  :root {
    --turquoise: #5cc6c6;
    --window: #dcf0f0;
    --paper: #ffffff;
    --ink: #1e1e1e;
    --backdrop: #e6e1dc;
    --clasp: #2e2e2e;
  }
  * { box-sizing: border-box; margin: 0; padding: 0; }
  html, body { width: 1200px; height: 677px; overflow: hidden; }
  body {
    background: var(--backdrop);
    font-family: "Hind", "Helvetica Neue", Arial, sans-serif;
    color: var(--ink);
    position: relative;
  }
  .sheet {
    position: absolute;
    background: var(--paper);
    box-shadow: 0 3px 8px rgba(0,0,0,.18);
    overflow: hidden;
  }
  .band {
    position: absolute;
    left: 0; right: 0; bottom: 0;
    background: var(--turquoise);
    color: #fff;
    font-weight: 600;
    letter-spacing: .08em;
    display: flex; align-items: center; justify-content: center;
  }
  .brand {
    position: absolute;
    text-align: center;
    color: var(--turquoise);
    line-height: 1;
  }
  .brand-dot {
    display: block;
    margin: 0 auto;
    background: var(--turquoise);
  }
  .brand-name {
    display: block;
    font-weight: 400;
    letter-spacing: .06em;
    text-transform: uppercase;
    white-space: nowrap;
    padding-bottom: .45em;
    border-bottom: 1px solid var(--turquoise);
  }
  .brand-tagline {
    display: block;
    letter-spacing: .08em;
    white-space: nowrap;
    padding-top: .55em;
    font-size: .85em;
  }
  .contact {
    position: absolute;
    line-height: 1.3;
    white-space: nowrap;
    font-style: normal;
  }
  .contact .street { letter-spacing: .06em; font-weight: 500; }
  .contact .gap { display: block; height: .8em; }
  .label { color: var(--turquoise); }

  /* Letter back */
  .letter-back { left: 78px; top: 101px; width: 336px; height: 474px; }
  .letter-back .band { height: 37px; font-size: 8px; }
  .clasp { position: absolute; left: 158px; top: 31px; width: 16px; height: 28px; background: var(--clasp); border-radius: 8px; }
  .letter-back .brand { left: 112px; top: 383px; font-size: 3.6px; }
  .letter-back .brand-dot { width: 18px; height: 18px; margin-bottom: 5px; }
  .letter-back .contact { left: 167px; top: 400px; font-size: 4.4px; }

  /* Letterhead */
  .letterhead { left: 435px; top: 108px; width: 326px; height: 460px; }
  .letterhead .band { height: 33px; font-size: 7.5px; }
  .letterhead .brand { left: 31px; top: 17px; font-size: 4.4px; }
  .letterhead .brand-dot { width: 22px; height: 22px; margin-bottom: 6px; }
  .letterhead .contact { left: 221px; top: 37px; font-size: 5.2px; }

  /* Window envelope */
  .envelope-window { left: 782px; top: 108px; width: 343px; height: 163px; }
  .envelope-window .band { height: 17px; font-size: 5.6px; justify-content: flex-end; padding-right: 20px; }
  .address-window { position: absolute; left: 18px; top: 71px; width: 159px; height: 69px; background: var(--window); border-radius: 5px; }
  .envelope-window .brand { left: 258px; top: 96px; font-size: 3.5px; }
  .envelope-window .brand-dot { width: 16px; height: 16px; margin-bottom: 5px; }

  /* Plain envelope */
  .envelope-plain { left: 783px; top: 292px; width: 343px; height: 163px; }
  .envelope-plain .band { height: 32px; font-size: 7.4px; }
  .envelope-plain .brand { left: 23px; top: 14px; font-size: 3.5px; }
  .envelope-plain .brand-dot { width: 17px; height: 17px; margin-bottom: 5px; }
  .envelope-plain .contact { left: 265px; top: 18px; font-size: 4.3px; }

  /* Business cards */
  .card-landscape { left: 783px; top: 481px; width: 158px; height: 87px; }
  .card-landscape .band { height: 18px; font-size: 5px; }
  .card-landscape .brand { left: 18px; top: 15px; font-size: 2.9px; }
  .card-landscape .brand-dot { width: 15px; height: 15px; margin-bottom: 4px; }
  .card-landscape .contact { left: 72px; top: 9px; width: 82px; text-align: center; font-size: 4.2px; }
  .card-portrait { left: 991px; top: 481px; width: 88px; height: 160px; }
  .card-portrait .band { height: 17px; font-size: 4.2px; }
  .card-portrait .brand { left: 0; right: 0; top: 45px; font-size: 3.4px; }
  .card-portrait .brand-name { display: inline-block; }
  .card-portrait .brand-dot { width: 17px; height: 17px; margin-bottom: 5px; }
  .card-portrait .contact { left: 0; right: 0; top: 8px; text-align: center; font-size: 4.4px; }
  .person { font-weight: 500; font-size: 1.25em; }
  .card-portrait .details { position: absolute; left: 0; right: 0; top: 102px; text-align: center; font-size: 4.4px; line-height: 1.35; font-style: normal; }
</style>
</head>
<body>

<section class="sheet letter-back">
  <div class="clasp" role="img" aria-label="String-and-button envelope clasp"></div>
  <div class="brand">
    <span class="brand-dot"></span>
    <span class="brand-name">Mercer Bay Fellowship</span>
    <span class="brand-tagline">One table, many homes</span>
  </div>
  <address class="contact">
    <span class="street">3-2-9 Kitamachi</span><br>
    <span class="street">Minato-ku 140-0012</span>
    <span class="gap"></span>
    <span class="label">Telephone:</span> (03) 5210-0318<br>
    <span class="label">Fax:</span> (03) 5210-0356<br>
    <span class="label">E-mail:</span> office@velmarhall.org
  </address>
  <div class="band">http://www.velmarhall.org</div>
</section>

<section class="sheet letterhead">
  <div class="brand">
    <span class="brand-dot"></span>
    <span class="brand-name">Mercer Bay Fellowship</span>
    <span class="brand-tagline">One table, many homes</span>
  </div>
  <address class="contact">
    <span class="street">3-2-9 Kitamachi</span><br>
    <span class="street">Minato-ku 140-0012</span>
    <span class="gap"></span>
    <span class="label">Telephone:</span> (03) 5210-0318<br>
    <span class="label">Fax:</span> (03) 5210-0356<br>
    <span class="label">E-mail:</span> office@velmarhall.org
  </address>
  <div class="band">http://www.velmarhall.org</div>
</section>

<section class="sheet envelope-window">
  <div class="address-window"></div>
  <div class="brand">
    <span class="brand-dot"></span>
    <span class="brand-name">Mercer Bay Fellowship</span>
    <span class="brand-tagline">One table, many homes</span>
  </div>
  <div class="band">http://www.velmarhall.org</div>
</section>

<section class="sheet envelope-plain">
  <div class="brand">
    <span class="brand-dot"></span>
    <span class="brand-name">Mercer Bay Fellowship</span>
    <span class="brand-tagline">One table, many homes</span>
  </div>
  <address class="contact">
    <span class="street">3-2-9 Kitamachi</span><br>
    <span class="street">Minato-ku 140-0012</span>
    <span class="gap"></span>
    <span class="label">Telephone:</span> (03) 5210-0318<br>
    <span class="label">Fax:</span> (03) 5210-0356<br>
    <span class="label">E-mail:</span> office@velmarhall.org
  </address>
  <div class="band">http://www.velmarhall.org</div>
</section>

<section class="sheet card-landscape">
  <div class="brand">
    <span class="brand-dot"></span>
    <span class="brand-name">Mercer Bay Fellowship</span>
    <span class="brand-tagline">One table, many homes</span>
  </div>
  <address class="contact">
    <span class="person">Rev. Daniel Okamoto</span><br>
    Pastor
    <span class="gap"></span>
    3-2-9 Kitamachi<br>
    Minato-ku 140-0012<br>
    <span class="label">Telephone:</span> (03) 5210-0318<br>
    <span class="label">Fax:</span> (03) 5210-0356<br>
    <span class="label">E-mail:</span> office@velmarhall.org
  </address>
  <div class="band">http://www.velmarhall.org</div>
</section>

<section class="sheet card-portrait">
  <div class="contact">
    <span class="person">Rev. Daniel Okamoto</span><br>
    Pastor
  </div>
  <div class="brand">
    <span class="brand-dot"></span>
    <span class="brand-name">Mercer Bay Fellowship</span>
    <span class="brand-tagline">One table, many homes</span>
  </div>
  <address class="details">
    3-2-9 Kitamachi<br>
    Minato-ku 140-0012<br><br>
    <span class="label">Telephone:</span> (03) 5210-0318<br>
    <span class="label">Fax:</span> (03) 5210-0356<br>
    <span class="label">E-mail:</span> office@velmarhall.org
  </address>
  <div class="band">http://www.velmarhall.org</div>
</section>

</body>
</html>
```